Develop a Website for a high end EBR/NLQ Test Preparation Company

The Tallowby Method provides a unique style of academic and educational assistance to consistently deliver improvements in grades, test scores, and college placement for students from a range of academic backgrounds. The Tallowby Method offers students customized options for coursework support, application coaching, and standardized test prep. Specializing in EBR and NLQ preparation, The Tallowby Method helps students increase their composite EBR score by 7+ points in several short months of prep time.

The Tallowby Method has the best EBR/NLQ track record in Chicago.

Our Delmont and All-Pell -Circle tutors help you efficiently add +7 EBR points and +250 NLQ and Subject Tests points

Target Market(s)

Educated parents - upper middle class in Business, finance, entrepreneurs, lawyers, professors

Industry/Entity Type

Education

Number of Pages Required

2 page

Font styles to use
Serif
Sans Serif

Colors

Designer to choose colors to be used in the design.

Requirements
Must have
• Please adhere to the attached wireframe and style guide

```html
<!DOCTYPE html>
<html lang="en">
<head>
<meta charset="utf-8">
<title>The Tallowby Method — Request a Consultation</title>
<link href="https://fonts.googleapis.com/css2?family=Poppins:wght@400;500;600&family=Tinos:ital,wght@0,700;1,700&display=swap" rel="stylesheet">
<style>
  :root{
    --page:#f2f2f2;
    --header:#f7f7f7;
    --hero:#3a3a3a;
    --brand:#7a1d18;
    --brand-dark:#5e0f0c;
    --ink:#1c1c1c;
    --muted:#8a8a8a;
    --line:#cfcfcf;
    --veil:rgba(35,35,35,.68);
    --frame:#9a9a9a;
  }
  *{box-sizing:border-box;margin:0;padding:0}
  html,body{width:1200px;height:625px;overflow:hidden}
  body{position:relative;background:var(--page);font-family:'Poppins',sans-serif;color:var(--ink)}

  .site-header{position:absolute;left:0;top:0;width:1200px;height:69px;background:var(--header)}
  .brand-name{position:absolute;left:235px;top:27px;width:150px;font-family:'Tinos',serif;font-weight:700;font-size:12px;color:var(--brand);white-space:nowrap}
  .main-nav{position:absolute;left:397px;top:32px;display:flex;gap:13px;font-size:7.5px;font-weight:500;color:#333;text-transform:uppercase;white-space:nowrap}
  .apply-btn{position:absolute;left:859px;top:11px;width:107px;height:48px;background:var(--brand);color:#fff;text-align:center;border-radius:2px;padding-top:5px}
  .apply-btn strong{display:block;font-size:10px;font-weight:600}
  .apply-btn span{display:block;font-size:5px;line-height:7px;padding:1px 8px 0}

  .hero{position:absolute;left:0;top:69px;width:1200px;height:375px;background:var(--hero)}
  .hero-photo{position:absolute;right:0;top:0;width:390px;height:375px;background:linear-gradient(135deg,#6b6a66,#b3a89a 55%,#8d96a0)}
  .hero-copy{position:absolute;left:235px;top:82px;color:#fff;white-space:nowrap}
  .hero-kicker{font-size:19px;font-weight:600}
  .hero-title{font-size:35px;font-weight:600;margin-top:2px}
  .hero-sub{font-size:12px;margin-top:2px}
  .hero-note{font-size:9px;margin-top:6px}
  .hero-btn{position:absolute;left:234px;top:225px;width:126px;height:54px;border:1px solid #fff;color:#fff;font-size:9px;font-weight:600;text-align:center;padding-top:12px;line-height:15px}

  .slider-dot{position:absolute;left:579px;top:535px;width:20px;height:2px;background:#333}
  .service{position:absolute;top:583px;width:230px;height:60px}
  .service .corner{position:absolute;left:0;top:0;width:50px;height:40px;border-left:3px solid var(--brand);border-top:3px solid var(--brand)}
  .service .label{position:absolute;left:0;width:240px;top:32px;text-align:center;font-size:12px;font-weight:500}
  .call-tab{position:absolute;left:1161px;top:499px;width:39px;height:140px;background:var(--brand)}
  .call-tab span{position:absolute;left:7px;top:108px;transform:rotate(-90deg);transform-origin:left top;color:#fff;font-size:9px;font-weight:600;white-space:nowrap;letter-spacing:.5px}

  .veil{position:absolute;inset:0;background:var(--veil)}

  .modal{position:absolute;left:374px;top:92px;width:452px;height:425px;background:#fff;border:3px solid var(--frame)}
  .modal-close{position:absolute;left:420px;top:24px}
  .modal-title{position:absolute;left:38px;top:28px;font-family:'Tinos',serif;font-style:italic;font-weight:700;font-size:23.5px;white-space:nowrap}
  .modal-lead{position:absolute;left:40px;top:73px;font-size:12.8px;white-space:nowrap}
  .perks{position:absolute;left:40px;top:104px;list-style:none;font-size:10.5px;line-height:16.3px}
  .perks li{padding-left:22px;position:relative}
  .perks li::before{content:"";position:absolute;left:11px;top:6px;width:4px;height:4px;border-radius:50%;background:#555}
  .field{position:absolute;left:40px;width:375px;height:36px;border:1px solid var(--line);font-size:11px;color:var(--muted);padding:0 13px;line-height:34px}
  .submit{position:absolute;left:172px;top:352px;width:108px;height:35px;border-radius:2px;background:linear-gradient(#9b2a22,var(--brand-dark));color:#fff;font-size:12px;font-weight:600;text-align:center;line-height:35px}
</style>
</head>
<body>
  <header class="site-header">
    <div class="brand-name">The Tallowby Method</div>
    <nav class="main-nav">
      <span>About Us</span><span>Our Concierge Services</span><span>The Tallowby Edge</span><span>Complimentary Consult</span><span>Contact Us</span>
    </nav>
    <div class="apply-btn"><strong>APPLY NOW</strong><span>AND GET A 30 MINUTE CONSULTATION WITH ONE OF OUR EXPERTS</span></div>
  </header>

  <section class="hero">
    <div class="hero-photo" role="img" aria-label="Photo of smiling students gathered around a laptop"></div>
    <div class="hero-copy">
      <div class="hero-kicker">Pell-Circle Ac</div>
      <div class="hero-title">Help St</div>
      <div class="hero-sub">Premier EBR/NLQ Test</div>
      <div class="hero-note">Serving Chicago and New York C</div>
    </div>
    <div class="hero-btn">Discover the Tallowby<br>Method</div>
  </section>

  <div class="slider-dot"></div>
  <div class="service" style="left:231px"><div class="corner"></div><div class="label">TEST PREP</div></div>
  <div class="service" style="left:481px"><div class="corner"></div><div class="label">EBR</div></div>
  <div class="service" style="left:731px"><div class="corner"></div><div class="label">NLQ</div></div>
  <div class="call-tab"><span>REQUEST A CALL</span></div>

  <div class="veil"></div>

  <div class="modal" role="dialog" aria-label="Request a consultation">
    <svg class="modal-close" width="13" height="13" viewBox="0 0 13 13" aria-label="Close">
      <circle cx="6.5" cy="6.5" r="5.8" fill="#fff" stroke="#999" stroke-width="1"/>
      <path d="M4.6 4.6l3.8 3.8M8.4 4.6l-3.8 3.8" stroke="#222" stroke-width="1.3"/>
    </svg>
    <h2 class="modal-title">Request A 30-Minute Consultation</h2>
    <p class="modal-lead">Bulleted list of what's included in the consultation</p>
    <ul class="perks">
      <li>30 Minute Consultation</li>
      <li>Meet and Greet</li>
      <li>Information Packet</li>
      <li>Bullet 4</li>
      <li>Bullet 5</li>
    </ul>
    <div class="field" style="top:196px">Name</div>
    <div class="field" style="top:242px">Email</div>
    <div class="field" style="top:288px">Phone Number</div>
    <div class="submit">SUBMIT</div>
  </div>
</body>
</html>
```